Website Design for new business Brightfield Junior Games

We need a website for our new business Brightfield Junior Games which is about teaching kids from 5 years to 16 years of age how to play either Australian Rules Football or Soccer. Need area for Soccer and Football plus Coaches section, and schedule for each training etc. NEW LOGO ADDED

Target Market(s)

Adults with kids from 5 to 16 looking for specialist coaches to train their kids

Industry/Entity Type

Fitness

Number of Pages Required

5+ page

Colors
3176b5
ffc214

Requirements
Must have
• Logo
• How, Why and What
Nice to have
• I like this website http://www.tallyhoopers.com.au/
• http://www.meadowkickdrills.com.au/ is another site that is okay
Should not have
• Our competitor is this website http://www.pitchcometschooling.com.au/ but I don't like their website style not kid or parent friendly

```html
<!DOCTYPE html>
<html lang="en">
<head>
<meta charset="utf-8">
<title>Brightfield Junior Games – Contact Us</title>
<link rel="stylesheet" href="https://fonts.googleapis.com/css2?family=Questrial&display=swap">
<style>
:root{
  --top-bar:#3a3a3a;
  --top-tab:#5a5a5a;
  --top-tab-edge:#6e6e6e;
  --search:#bdbdbd;
  --brand-yellow:#ffc214;
  --brand-blue:#3176b5;
  --nav-active:#1f6fd0;
  --field-white:#ffffff;
  --ink:#111111;
  --footer-green:#66a300;
  --base-black:#050505;
  --white:#ffffff;
  --social-sky:#1ea0e6;
  --social-red:#d42a26;
  --social-navy:#34508f;
  --social-blue:#0f76b5;
}
*{margin:0;padding:0;box-sizing:border-box}
html,body{width:1200px;height:1154px;overflow:hidden;background:#fff}
body{font-family:"Questrial",sans-serif;position:relative}
.page{position:relative;width:1200px;height:1154px}

.top-bar{position:absolute;left:0;top:0;width:1200px;height:60px;background:var(--top-bar)}
.top-tab{position:absolute;top:0;height:57px;background:var(--top-tab);border:2px solid var(--top-tab-edge);border-top:none;color:var(--white);font-size:24px;display:flex;align-items:center;justify-content:center}
.top-tab.about{left:90px;width:172px}
.top-tab.contact{left:267px;width:174px}
.search-box{position:absolute;left:845px;top:16px;width:260px;height:31px;background:var(--search);border:1px solid #9a9a9a}

.header-banner{position:absolute;left:0;top:60px;width:1200px;height:140px;background:linear-gradient(180deg,#3c78b8 0%,#4d8c4c 25%,#3f9a35 60%,#2f7d2e 100%)}
.brand-block{position:absolute;left:24px;top:83px;width:441px;height:108px;background:var(--brand-yellow);display:flex;align-items:center;justify-content:center}
.brand-name{color:var(--white);font-size:38px;line-height:1}

.main-nav{position:absolute;left:0;top:200px;width:1200px;height:60px;background:var(--brand-blue);border-radius:8px 8px 0 0;display:flex;padding-left:93px}
.nav-item{height:60px;display:flex;align-items:center;justify-content:center;color:var(--white);font-size:24px;padding:0 30px}
.nav-item.active{width:159px;background:var(--nav-active)}

.stage{position:absolute;left:0;top:260px;width:1200px;height:615px;background:linear-gradient(180deg,#7c7c7c 0%,#777 60%,#6a7a5c 85%,#4f6b3a 100%)}
.contact-title{position:absolute;left:120px;top:292px;font-size:44px;color:var(--white);font-weight:400}
.field{position:absolute;left:123px;background:var(--field-white)}
.field.name{top:368px;width:329px;height:39px}
.field.email{top:426px;width:329px;height:39px}
.field.message{top:480px;width:492px;height:261px}
.send-button{position:absolute;left:123px;top:782px;width:168px;height:49px;background:var(--field-white);color:var(--ink);font-size:36px;display:flex;align-items:center;padding-left:20px}
.company-details{position:absolute;right:139px;top:356px;text-align:right;color:var(--ink);font-size:31px;line-height:47px;font-style:normal}

.site-footer{position:absolute;left:0;top:875px;width:1200px;height:240px;background:var(--footer-green)}
.footer-col{position:absolute;top:919px;display:flex;flex-direction:column;gap:36px;color:var(--white);font-size:19px;line-height:22px}
.footer-col.first{left:137px}
.footer-col.second{left:317px}
.social-list{position:absolute;left:830px;top:1017px;display:flex;gap:16px}
.social-tile{width:58px;height:57px;border-radius:9px;box-shadow:0 2px 3px rgba(0,0,0,.35)}
.social-tile.sky{background:var(--social-sky)}
.social-tile.red{background:var(--social-red)}
.social-tile.navy{background:var(--social-navy)}
.social-tile.blue{background:var(--social-blue)}

.base-bar{position:absolute;left:0;top:1115px;width:1200px;height:39px;background:var(--base-black);color:var(--white);font-size:19px}
.base-bar span{position:absolute;top:9px}
</style>
</head>
<body>
<div class="page">
  <div class="top-bar">
    <div class="top-tab about">About</div>
    <div class="top-tab contact">Contact</div>
    <div class="search-box" aria-label="Search"></div>
  </div>

  <div class="header-banner" role="img" aria-label="Photo of a football stadium pitch with crowd stands"></div>
  <div class="brand-block"><span class="brand-name">Brightfield Junior Games</span></div>

  <nav class="main-nav">
    <div class="nav-item active">Home</div>
    <div class="nav-item">Soccer</div>
    <div class="nav-item">Football</div>
    <div class="nav-item">Coaches</div>
    <div class="nav-item">Schedule</div>
  </nav>

  <section class="stage" role="img" aria-label="Faded photo of a young footballer in kit crouching on a bench beside a ball on grass"></section>
  <h1 class="contact-title">Contact Us</h1>
  <div class="field name" aria-label="Your name"></div>
  <div class="field email" aria-label="Your email"></div>
  <div class="field message" aria-label="Your message"></div>
  <div class="send-button">SEND</div>
  <address class="company-details">
    Brightfield Junior Games<br>12 Wattle Street<br>Greenvale VIC 3059<br>(03) 9000 1234<br>hello@bjgames.com.au
  </address>

  <footer class="site-footer"></footer>
  <div class="footer-col first">
    <span>About Us</span>
    <span>Soccer</span>
    <span>Football</span>
  </div>
  <div class="footer-col second">
    <span>Coaches</span>
    <span>Schedule</span>
    <span>Gallery</span>
  </div>
  <div class="social-list">
    <div class="social-tile sky" aria-label="Social link"></div>
    <div class="social-tile red" aria-label="Video link"></div>
    <div class="social-tile navy" aria-label="Social link"></div>
    <div class="social-tile blue" aria-label="Social link"></div>
  </div>

  <div class="base-bar">
    <span style="left:90px">Copyright 2016- 2017</span>
    <span style="left:845px">Privacy Policy</span>
    <span style="left:1007px">Disclaimer</span>
  </div>
</div>
</body>
</html>
```